National Australian HR & Recruitment Company

we need a document design (letter head / footer) for a proposal document to send to clients. This needs to include a design for the front page and some kind of water mark or design throughout the document.
The document needs to remain workable (word.doc) not PDF
The design should be elegant and corporate looking
The document is attached

Target Market(s)

Human Resource Managers. Corporate Clients

Industry/Entity Type

It Company

Font styles to use
Sans Serif

Requirements
Must have
• Must have a sleek elegant look

```html
<!DOCTYPE html>
<html lang="en">
<head>
<meta charset="utf-8">
<title>Crestway – Proposal Stationery</title>
<link href="https://fonts.googleapis.com/css2?family=Open+Sans:wght@400;600;700&display=swap" rel="stylesheet">
<style>
  :root {
    --teal: #1fa39a;
    --grey: #6b6b6b;
    --ink: #4a4a4a;
    --paper: #ffffff;
    --backdrop: #e9ebec;
  }
  * { box-sizing: border-box; margin: 0; padding: 0; }
  html, body {
    width: 1200px; height: 800px; overflow: hidden;
    background: var(--backdrop);
    font-family: "Open Sans", Arial, sans-serif;
  }
  .stationery { position: relative; width: 1200px; height: 800px; }
  .page {
    position: absolute; top: 66px;
    width: 470px; height: 668px;
    background: var(--paper);
    box-shadow: 0 6px 22px rgba(0,0,0,.18);
    overflow: hidden;
  }
  .page--cover { left: 90px; }
  .page--letter { left: 640px; }
  .page-art { position: absolute; inset: 0; width: 100%; height: 100%; }

  /* cover */
  .cover-brand {
    position: absolute; left: 0; right: 0; top: 250px;
    text-align: center;
  }
  .cover-brand__mark {
    width: 64px; height: 64px; border-radius: 50%;
    background: var(--teal); margin: 0 auto 20px;
  }
  .cover-brand__name {
    font-weight: 700; font-size: 58px; letter-spacing: -1px;
    color: var(--grey); line-height: 1;
  }

  /* letter */
  .letter-brand {
    position: absolute; left: 30px; top: 62px;
    display: flex; align-items: center; gap: 7px;
  }
  .letter-brand__mark { width: 14px; height: 14px; border-radius: 50%; background: var(--teal); }
  .letter-brand__name { font-weight: 700; font-size: 20px; color: var(--grey); letter-spacing: -.3px; }
  .letter-body {
    position: absolute; left: 40px; right: 40px; top: 110px;
    font-size: 8.4px; line-height: 1.5; color: var(--ink);
  }
  .letter-body p { margin-bottom: 8px; }
  .signature-line { width: 90px; height: 22px; border-bottom: 1px solid var(--ink); margin: 6px 0 4px; }
  .signatory { line-height: 1.35; }
  .letter-footer {
    position: absolute; left: 30px; bottom: 12px;
    font-size: 9px; font-weight: 600; color: #fff; letter-spacing: .3px;
  }
</style>
</head>
<body>
<main class="stationery">

  <section class="page page--cover">
    <svg class="page-art" viewBox="0 0 470 668" preserveAspectRatio="none" aria-hidden="true">
      <path d="M0 0 H470 V22 C320 24 160 45 0 120 Z" fill="var(--teal)"/>
      <path d="M0 668 V588 C160 596 330 600 470 500 V668 Z" fill="var(--teal)"/>
      <path d="M0 668 V606 C160 612 330 615 470 524 V668 Z" fill="var(--grey)"/>
    </svg>
    <div class="cover-brand">
      <div class="cover-brand__mark"></div>
      <div class="cover-brand__name">Crestway</div>
    </div>
  </section>

  <section class="page page--letter">
    <svg class="page-art" viewBox="0 0 470 668" preserveAspectRatio="none" aria-hidden="true">
      <path d="M0 0 H470 V14 C320 14 150 20 0 52 Z" fill="var(--teal)"/>
      <path d="M0 668 V618 C170 628 330 618 470 560 V668 Z" fill="var(--teal)"/>
      <path d="M0 668 V632 C170 640 330 632 470 585 V668 Z" fill="var(--grey)"/>
    </svg>
    <header class="letter-brand">
      <span class="letter-brand__mark"></span>
      <span class="letter-brand__name">Crestway</span>
    </header>
    <article class="letter-body">
      <p>Dear Priya,</p>
      <p>Thank you for reaching out to Crestway to offer us the opportunity to assist your employees through our outplacement and career transition services.</p>
      <p>We understand that as a responsible employer, providing outplacement is about much more than managing employment legislation; it is about safeguarding your employer brand and caring for your people.</p>
      <p>However, when looking to provide outplacement support for your staff, it is hard to balance cost and quality. Our programs are tailored, meaningful and effective for each employee without breaking the budget.</p>
      <p>We work with you to create high impact, tailored and cost effective support for your employees, with programs built around practical career transition support that gives them confidence to define their own path.</p>
      <p>Our essentials cover Job Search Strategy, Resume Tips, Advice on Applying for Jobs, the Hidden Job Market, Networking and Social Media, Recruitment Agencies, Interview Preparation and Coping with Change.</p>
      <p>We have provided program options to suit your unique needs, the details of which are outlined in the following pages.</p>
      <p>We pride ourselves on our ability to be flexible and will tailor our programs to you, so please ask if there is anything else we can do.</p>
      <p>We look forward to being of assistance.</p>
      <div class="letter-signoff">
        <p>Warm regards,</p>
        <div class="signature-line"></div>
        <p class="signatory">Lena Marsh<br>General Manager</p>
      </div>
    </article>
    <footer class="letter-footer">www.crestwayaustralia.com.au</footer>
  </section>

</main>
</body>
</html>
```